318 Diamond & Fastpitch Clinic 2017

Design a flyer that will promote our 2017 summer camp for boys and girls softball.

Weeks of
July 10th - 14th
July 17th - 21st.

Players ages 5 - 11.
Full day = 9:30am - 2:30pm half day = 9:30am - 11:30am.
$295 / full day : $195/ half day

Hosted by "318 Diamond" affiliated with the KV Meteors Touring Baseball & Softball Club and the Pine Hollow Junior League,

Camp Location PHJL, Lane 48C Maple Bluff.

PHone 555-284-7730, email info@318diamond.example

The color should be "Red white and blue color scheme" with dates and location standing out. 318 Logo should be prominent PHJL and Meteors smaller and secondary.

Feel free to use stock photo's if available. visit www.kvmeteors.example for more pictures and there are links for the 2017 summer camp there with possibly some more information.

Target Market(s)

to catch the eye of parents of players ages 5 - 11 already at little league or shopping in local stores

Colors
ec1f27
0355a3
ffffff

Requirements
Must have
• red white and blue design,
• 318 logo and summer camp prominent so it catches the eye and explains what it is right away.
• the meteors and pine hollow logo's a the bottom showing the affiliation.
Nice to have
• stock photo's or something showing players having a great time or a beautiful ballpark
Should not have
• to much clutter or hard to figure out what it's for

```html
<!DOCTYPE html>
<html lang="en">
<head>
<meta charset="utf-8">
<title>318 Diamond &amp; Fastpitch Clinic 2017 – Summer Camp</title>
<link rel="stylesheet" href="https://fonts.googleapis.com/css2?family=Alfa+Slab+One&family=Bungee&family=Roboto:wght@500;700&display=swap">
<style>
  :root {
    --red: #ec1f27;
    --blue: #0355a3;
    --navy: #1b2a55;
    --white: #ffffff;
    --ink: #222222;
    --shade: #2b2b2b;
    --rule: #9a9a9a;
    --pine: #3c8a3a;
    --silver-top: #ffffff;
    --silver-bottom: #9b9b9b;
  }
  * { box-sizing: border-box; margin: 0; padding: 0; }
  html, body { width: 850px; height: 1200px; overflow: hidden; background: var(--white); }
  .flyer { position: relative; width: 850px; height: 1200px; background: var(--white); font-family: "Bungee", sans-serif; }
  .artwork { position: absolute; inset: 0; }

  .brand { position: absolute; left: 50px; top: 40px; width: 210px; text-align: center; color: var(--red); font-family: "Alfa Slab One", serif; line-height: 1; }
  .brand__number { display: block; font-size: 96px; letter-spacing: 2px; }
  .brand__name { display: block; font-size: 26px; letter-spacing: 4px; margin-top: 4px; }

  .dates { position: absolute; left: 527px; top: 32px; }
  .dates__label { color: var(--red); font-size: 24px; line-height: 1.2; }
  .dates__week { color: var(--blue); font-size: 23px; line-height: 1.25; }

  .schedule { position: absolute; left: 50px; top: 866px; width: 366px; height: 176px; border: 2px solid var(--blue); border-radius: 12px; background: var(--white); }
  .schedule__partners { position: absolute; top: 12px; left: 0; right: 0; display: flex; justify-content: center; align-items: center; gap: 18px; }
  .partner { font-family: "Alfa Slab One", serif; line-height: 1; }
  .partner--meteors { background: var(--navy); color: var(--white); padding: 14px 12px; font-size: 21px; }
  .partner--pine { color: var(--pine); font-size: 15px; text-align: center; width: 80px; }
  .schedule__cols { position: absolute; left: 0; right: 0; top: 90px; display: flex; }
  .schedule__col { flex: 1; text-align: center; }
  .schedule__col + .schedule__col { border-left: 1.5px solid var(--ink); }
  .schedule__label { color: var(--red); font-size: 18px; line-height: 1.2; }
  .schedule__time { color: var(--ink); font-size: 19px; line-height: 1.05; }
  .schedule__dash { color: var(--ink); font-size: 14px; line-height: 0.6; }

  .pricing { position: absolute; left: 433px; top: 866px; width: 394px; height: 176px; background: var(--blue); border-radius: 16px; display: flex; align-items: center; }
  .pricing__option { flex: 1; text-align: center; }
  .pricing__option + .pricing__option { border-left: 3px dotted var(--white); }
  .pricing__label { color: var(--white); font-size: 24px; line-height: 1.3; }
  .pricing__amount { color: var(--red); font-family: "Alfa Slab One", serif; font-size: 52px; line-height: 1.1; }

  .location { position: absolute; left: 50px; top: 1069px; width: 749px; height: 54px; border: 1.5px solid var(--rule); display: flex; align-items: center; justify-content: center; color: var(--red); font-size: 22px; }
  .location__pin { position: absolute; left: 411px; top: 1046px; width: 36px; height: 36px; background: var(--white); border-radius: 50%; }

  .contact { position: absolute; left: 28px; right: 28px; top: 1136px; height: 46px; display: flex; align-items: center; justify-content: center; }
  .contact__phone { color: var(--red); font-size: 24px; }
  .contact__phone span { color: var(--ink); font-family: "Roboto", sans-serif; font-weight: 500; font-size: 26px; }
  .contact__divider { width: 1.5px; height: 40px; background: var(--ink); margin: 0 20px; }
  .contact__mail { display: flex; align-items: center; gap: 10px; color: var(--red); font-size: 22px; }
  .footer-band { position: absolute; left: 0; right: 0; bottom: 0; height: 10px; background: var(--blue); }
</style>
</head>
<body>
<main class="flyer">
  <svg class="artwork" width="850" height="1200" viewBox="0 0 850 1200" xmlns="http://www.w3.org/2000/svg">
    <defs>
      <linearGradient id="field" x1="0" y1="0" x2="0" y2="1">
        <stop offset="0" stop-color="#9cc3e0"/>
        <stop offset="0.45" stop-color="#8fb36a"/>
        <stop offset="1" stop-color="#c9a27c"/>
      </linearGradient>
      <linearGradient id="batter" x1="0" y1="0" x2="0" y2="1">
        <stop offset="0" stop-color="#7fa8d6"/>
        <stop offset="0.45" stop-color="#dfe6f1"/>
        <stop offset="1" stop-color="#2f58ad"/>
      </linearGradient>
      <linearGradient id="silver" x1="0" y1="0" x2="0" y2="1">
        <stop offset="0" stop-color="var(--silver-top)"/>
        <stop offset="1" stop-color="var(--silver-bottom)"/>
      </linearGradient>
    </defs>

    <g class="photos">
      <polygon role="img" aria-label="Photo: young player in white and navy uniform with glove" points="44,255 204,242 204,640 44,650" fill="url(#field)"/>
      <polygon role="img" aria-label="Photo: player reaching to catch a ball" points="236,235 406,219 406,598 236,604" fill="url(#field)"/>
      <polygon role="img" aria-label="Photo: player in red helmet at the plate" points="460,182 635,165 635,558 460,574" fill="url(#field)"/>
      <polygon role="img" aria-label="Photo: player number 22 kneeling with bat" points="644,155 814,130 814,484 644,528" fill="url(#field)"/>
      <polygon role="img" aria-label="Photo: batter in blue helmet ready to swing" points="300,150 590,120 590,560 300,628" fill="url(#batter)"/>
    </g>

    <g class="bands">
      <polygon points="47,690 814,508 814,626 47,808" fill="var(--blue)"/>
      <polygon points="310,804 814,685 814,743 310,862" fill="var(--blue)"/>
    </g>

    <g class="headline" transform="translate(47 690) rotate(-13.3)">
      <text x="399" y="96" text-anchor="middle" font-family="Alfa Slab One, serif" font-size="72" textLength="700" lengthAdjust="spacingAndGlyphs" fill="var(--shade)">2017 SUMMER CAMP</text>
      <text x="395" y="92" text-anchor="middle" font-family="Alfa Slab One, serif" font-size="72" textLength="700" lengthAdjust="spacingAndGlyphs" fill="url(#silver)">2017 SUMMER CAMP</text>

      <text x="130" y="165" font-family="Alfa Slab One, serif" font-size="40" textLength="90" lengthAdjust="spacingAndGlyphs" fill="var(--ink)">FOR</text>
      <text x="240" y="165" font-family="Alfa Slab One, serif" font-size="64" textLength="200" lengthAdjust="spacingAndGlyphs" fill="var(--red)">BOYS</text>
      <text x="455" y="165" font-family="Alfa Slab One, serif" font-size="50" fill="var(--ink)">&amp;</text>
      <text x="520" y="165" font-family="Alfa Slab One, serif" font-size="64" textLength="225" lengthAdjust="spacingAndGlyphs" fill="var(--red)">GIRLS</text>

      <text x="394" y="225" font-family="Alfa Slab One, serif" font-size="58" textLength="340" lengthAdjust="spacingAndGlyphs" fill="var(--shade)">SOFTBALL</text>
      <text x="390" y="221" font-family="Alfa Slab One, serif" font-size="58" textLength="340" lengthAdjust="spacingAndGlyphs" fill="url(#silver)">SOFTBALL</text>
    </g>

    <g class="ages">
      <text transform="translate(806 790) rotate(-13.3)" text-anchor="end" font-family="Bungee, sans-serif" font-size="23" textLength="200" lengthAdjust="spacingAndGlyphs" fill="var(--blue)">Players ages</text>
      <text transform="translate(806 832) rotate(-13.3)" text-anchor="end" font-family="Bungee, sans-serif" font-size="30" textLength="82" lengthAdjust="spacingAndGlyphs" fill="var(--red)">5-11</text>
    </g>
  </svg>

  <div class="brand">
    <span class="brand__number">318</span>
    <span class="brand__name">DIAMOND</span>
  </div>

  <div class="dates">
    <p class="dates__label">Weeks of</p>
    <p class="dates__week">July 10th - 14th</p>
    <p class="dates__week">July 17th - 21st</p>
  </div>

  <section class="schedule">
    <div class="schedule__partners">
      <span class="partner partner--meteors">KV METEORS</span>
      <span class="partner partner--pine">Pine Hollow</span>
    </div>
    <div class="schedule__cols">
      <div class="schedule__col">
        <p class="schedule__label">Full Day</p>
        <p class="schedule__time">9:30am</p>
        <p class="schedule__dash">-</p>
        <p class="schedule__time">2:30pm</p>
      </div>
      <div class="schedule__col">
        <p class="schedule__label">Half Day</p>
        <p class="schedule__time">9:30am</p>
        <p class="schedule__dash">-</p>
        <p class="schedule__time">11:30am.</p>
      </div>
    </div>
  </section>

  <section class="pricing">
    <div class="pricing__option">
      <p class="pricing__label">Full Day</p>
      <p class="pricing__amount">$295</p>
    </div>
    <div class="pricing__option">
      <p class="pricing__label">Half Day</p>
      <p class="pricing__amount">$195</p>
    </div>
  </section>

  <p class="location">Camp Location PHJL, Lane 48C Maple Bluff.</p>
  <svg class="location__pin" viewBox="0 0 36 36" aria-hidden="true">
    <path d="M18 5 C12 5 9 9.5 9 14 C9 20 18 30 18 30 C18 30 27 20 27 14 C27 9.5 24 5 18 5 Z" fill="var(--blue)"/>
    <circle cx="18" cy="14" r="3.5" fill="#fff"/>
  </svg>

  <footer class="contact">
    <p class="contact__phone">Call us: <span>555-284-7730</span></p>
    <div class="contact__divider"></div>
    <p class="contact__mail">
      <svg width="26" height="26" viewBox="0 0 26 26" aria-hidden="true">
        <circle cx="13" cy="13" r="12" fill="var(--ink)"/>
        <rect x="6.5" y="8.5" width="13" height="9" fill="none" stroke="#fff" stroke-width="1.5"/>
        <path d="M6.5 8.5 L13 13.5 L19.5 8.5" fill="none" stroke="#fff" stroke-width="1.5"/>
      </svg>
      info@318diamond.example
    </p>
  </footer>
  <div class="footer-band"></div>
</main>
</body>
</html>
```